Web Design Project - Tallow Analytics

I am a Mechanical Engineer running a one person consulting firm at this point. The hope is to expand in the future, but for now I simply need a website that conveys a professional appearance, and allows potential and existing clients to find me. Website design displaying contact information, CV for download, capabilities, past projects, etc. I've included four examples below from companies that provided the same service. I've only provided these as general reference for the type of work I do and how others have chosen to display this information. The design is completely at your discretion.

I've included the current Logo in the uploaded files section. I will provide content as requried.

http://www.quorvelmo.com/
http://www.truvane.com/
http://www.palqinsystems.com/
http://brindlowmechanics.net/

Industry/Entity Type

Consulting

```html
<!DOCTYPE html>
<html lang="en">
<head>
<meta charset="utf-8">
<title>Tallow Analytics – Engineering Consultants</title>
<link rel="stylesheet" href="https://fonts.googleapis.com/css2?family=Source+Sans+3:wght@400;600;700&family=Oswald:wght@500&display=swap">
<style>
:root{
  --orange:#d9782e;
  --orange-light:#f0a055;
  --orange-dark:#c9691f;
  --grey-band:#6f7475;
  --text:#3a3a3a;
  --muted:#555;
  --rule:#dcdcdc;
  --white:#fff;
  --footer-top:#e9e9e9;
  --footer-bot:#f7f7f7;
}
*{box-sizing:border-box;margin:0;padding:0}
html,body{width:1029px;height:1200px;overflow:hidden;background:var(--white)}
body{position:relative;font-family:"Source Sans 3",Arial,sans-serif;color:var(--text)}
.abs{position:absolute}

/* header */
.brand{left:111px;top:22px;display:flex;align-items:center;gap:10px}
.brand-mark{width:30px;height:30px;background:var(--orange)}
.brand-name{font-size:32px;font-weight:600;color:var(--orange);letter-spacing:.5px}
.brand-tag{left:154px;top:84px;font-size:9.5px;letter-spacing:1.6px;color:#666;font-weight:600}
.contact-top{right:112px;top:36px;text-align:right;font-size:14px;color:#666;font-weight:600;line-height:23px}
.contact-top .phone{color:var(--orange);font-size:16px}
.contact-top .mail{color:var(--orange);font-weight:400;font-size:12.5px}

/* nav */
.nav{left:111px;top:109px;width:806px;height:41px;border-radius:3px;
  background:linear-gradient(#f2a45b,#dc7a2c);border:1px solid var(--orange-dark);display:flex}
.nav a{color:var(--white);text-decoration:none;font-size:14px;display:flex;align-items:center;
  padding:0 19.5px;border-right:1px solid rgba(150,70,10,.45);box-shadow:1px 0 0 rgba(255,255,255,.25)}
.nav a:last-child{border-right:0;box-shadow:none;flex:1;justify-content:center}

/* slider */
.slider{left:111px;top:156px;width:806px;height:294px;border:1px solid #cfcfcf;border-radius:3px;background:var(--white);
  box-shadow:0 6px 8px -6px rgba(0,0,0,.35)}
.slide{position:absolute;left:3px;top:3px;right:3px;bottom:3px;
  background:linear-gradient(100deg,#e98a45 0%,#e5e5e3 25%,#f0f0ee 55%,#e8e8e6 75%,#d84030 88%,#e0d23a 100%)}
.dots{left:470px;top:421px;display:flex;gap:7px}
.dots span{width:16px;height:16px;border-radius:50%;background:#888}
.dots span:first-child{background:#333}

/* band */
.band{left:0;top:530px;width:1029px;height:285px;background:var(--grey-band)}
.h2{font-size:21px;color:var(--orange);font-weight:400}
.welcome-h{left:113px;top:499px}
.welcome-img{left:111px;top:543px;width:258px;height:114px;border:3px solid var(--white);
  background:linear-gradient(120deg,#c9cfd2,#d23a2e 40%,#7a7d70 70%,#a9a48f)}
.welcome-p{left:111px;top:669px;width:260px;font-size:11.5px;line-height:20px;color:var(--white)}
.btn{background:linear-gradient(#f5aa66,#e8853d);color:var(--white);font-size:12px;font-weight:600;
  border-radius:3px;display:flex;align-items:center;justify-content:center}
.readmore{left:111px;top:768px;width:69px;height:23px}

.projects{left:386px;top:496px;width:531px;height:297px;background:#f6f6f6;border:1px solid #d6d6d6;border-radius:3px;
  box-shadow:0 3px 0 #4f5354}
.projects-h{left:14px;top:7px}
.thumb{position:absolute;width:162px;height:89px;border:3px solid var(--white);outline:1px solid #cfcfcf;border-radius:3px}
.view-all{left:449px;top:257px;width:69px;height:24px;font-size:12.5px}

/* lower */
.col-h{top:829px}
.cap-list{left:111px;top:866px;width:241px;list-style:none}
.cap-list li{height:24px;border-bottom:1px dashed #d2d2d2;display:flex;align-items:center;font-size:11px;color:var(--muted)}
.cap-list li:last-child{border-bottom:0}
.cap-list svg{margin:0 11px 0 1px}
.more-link{font-size:11.5px;font-weight:700;color:var(--orange);letter-spacing:.3px}
.vrule{top:836px;width:1px;height:228px;background:var(--rule)}
.post{left:400px;width:238px}
.post h3{font-size:12.5px;font-weight:600;color:#222;line-height:17px}
.post p{font-size:11px;color:var(--muted);margin-top:2px}
.post time{display:block;font-size:10px;color:var(--orange);margin-top:4px}
.post-rule{left:400px;top:950px;width:238px;border-top:1px dashed #d2d2d2}

.cv-btn{left:674px;top:835px;width:218px;height:45px;border-radius:3px;
  background:linear-gradient(#6a6a6a,#3c3c3c);display:flex;align-items:center;gap:10px;padding-left:14px}
.cv-btn span{font-family:Oswald,"Arial Narrow",sans-serif;font-weight:500;font-size:21px;color:var(--white);letter-spacing:.5px}
.info{left:674px;top:924px;font-size:11px;color:var(--muted);line-height:17px}
.info h4{font-size:12.5px;font-weight:600;color:#222;margin-top:5px}
.info h4:first-child{margin-top:0}
.info a{color:var(--orange);text-decoration:none}

/* footer */
.footer{left:0;top:1086px;width:1029px;height:114px;background:linear-gradient(var(--footer-top),var(--footer-bot))}
.f-brand{left:111px;top:1100px;display:flex;align-items:center;gap:7px}
.f-brand .brand-mark{width:20px;height:20px;background:#8a8a8a}
.f-brand .brand-name{font-size:21px;color:#7a7a7a}
.f-tag{left:142px;top:1139px;font-size:7px;letter-spacing:1.2px;color:#666;font-weight:600}
.copy{left:111px;top:1157px;font-size:11px;color:#555}
.connect{left:757px;top:1105px;font-size:12.5px;color:#333;font-weight:600}
.social{left:759px;top:1132px;display:flex;gap:7px}
.social span{width:26px;height:26px;border-radius:3px;background:#9a9a9a;display:block}
</style>
</head>
<body>

<header>
  <div class="abs brand"><span class="brand-mark"></span><span class="brand-name">Tallow Analytics</span></div>
  <div class="abs brand-tag">ENGINEERING CONSULTANTS</div>
  <div class="abs contact-top">
    <div>Call Toll Free : <span class="phone">123 456 7890</span></div>
    <div>Email : <span class="mail">info@tallowanalytics.com</span></div>
  </div>
  <nav class="abs nav">
    <a href="#">Home</a><a href="#">About Us</a><a href="#">Services Offered</a><a href="#">Capabilities</a>
    <a href="#">Our Projects</a><a href="#">CV Downloads</a><a href="#">Contact Us</a>
  </nav>
</header>

<section class="abs slider">
  <div class="slide" role="img" aria-label="Close-up of a multimeter, test probes and a screwdriver lying on electrical floor plans"></div>
</section>
<div class="abs dots"><span></span><span></span><span></span><span></span></div>

<div class="abs band"></div>
<h2 class="abs h2 welcome-h">Welcome to Our Site</h2>
<div class="abs welcome-img" role="img" aria-label="Two engineers in hard hats reviewing drawings at an industrial site"></div>
<p class="abs welcome-p">Aliquam molestie, mi et imperdiet euismod, dui purus auctor tellus, et interdum lacus lectus et ante. Sed accumsan sollicitudin sapien, sit amet adipisc-ing turpis gravida ac.</p>
<a class="abs btn readmore">Read More</a>

<section class="abs projects">
  <h2 class="abs h2 projects-h">Our Projects</h2>
  <div class="thumb" style="left:14px;top:46px;background:linear-gradient(160deg,#6d8aa8,#3a3f3c 50%,#7d6e5a)" role="img" aria-label="Open-pit mine"></div>
  <div class="thumb" style="left:186px;top:46px;background:linear-gradient(#3c6d9c,#c58a2a 60%,#2d5680)" role="img" aria-label="Offshore oil platform"></div>
  <div class="thumb" style="left:357px;top:46px;background:linear-gradient(90deg,#6b3a24,#b98a60 50%,#5a4636)" role="img" aria-label="Turbine blades in a generator"></div>
  <div class="thumb" style="left:14px;top:149px;background:linear-gradient(#c5c9cc,#6d7276 60%,#b1aca5)" role="img" aria-label="Car on a crash test rig"></div>
  <div class="thumb" style="left:186px;top:149px;background:linear-gradient(90deg,#2b2b2b,#3f9a4c 45%,#222)" role="img" aria-label="Green circuit board"></div>
  <div class="thumb" style="left:357px;top:149px;background:linear-gradient(90deg,#8a7c68,#4f6650 50%,#b25048)" role="img" aria-label="Timber pilings at a harbour with a boat"></div>
  <a class="abs btn view-all">View All</a>
</section>

<section>
  <h2 class="abs h2 col-h" style="left:111px">Capabilities</h2>
  <ul class="abs cap-list">
    <li><svg width="12" height="11" viewBox="0 0 12 11"><path d="M1 6l3 3 7-8" fill="none" stroke="#e07a2a" stroke-width="2.4"/></svg>Et interdum lacus lectus et ante.</li>
    <li><svg width="12" height="11" viewBox="0 0 12 11"><path d="M1 6l3 3 7-8" fill="none" stroke="#e07a2a" stroke-width="2.4"/></svg>Sed accumsan sollicitudin sapien.</li>
    <li><svg width="12" height="11" viewBox="0 0 12 11"><path d="M1 6l3 3 7-8" fill="none" stroke="#e07a2a" stroke-width="2.4"/></svg>Sit amet adipiscing turpis.</li>
    <li><svg width="12" height="11" viewBox="0 0 12 11"><path d="M1 6l3 3 7-8" fill="none" stroke="#e07a2a" stroke-width="2.4"/></svg>Et interdum lacus lectus et ante.</li>
    <li><svg width="12" height="11" viewBox="0 0 12 11"><path d="M1 6l3 3 7-8" fill="none" stroke="#e07a2a" stroke-width="2.4"/></svg>Sed accumsan sollicitudin sapien.</li>
    <li><svg width="12" height="11" viewBox="0 0 12 11"><path d="M1 6l3 3 7-8" fill="none" stroke="#e07a2a" stroke-width="2.4"/></svg>Sit amet adipiscing turpis.</li>
    <li><svg width="12" height="11" viewBox="0 0 12 11"><path d="M1 6l3 3 7-8" fill="none" stroke="#e07a2a" stroke-width="2.4"/></svg>Sed accumsan sollicitudin sapien.</li>
  </ul>
  <a class="abs more-link" style="left:111px;top:1055px">READ MORE &gt;&gt;</a>
</section>
<div class="abs vrule" style="left:377px"></div>

<section>
  <h2 class="abs h2 col-h" style="left:400px">Blog Post</h2>
  <article class="abs post" style="top:867px">
    <h3>Fusce accumsan, elit a suscipit sagittis, tortor sapien cursus risus..</h3>
    <p>Et interdum lacus lectus et ante.</p>
    <time>on June 04, 2013</time>
  </article>
  <div class="abs post-rule"></div>
  <article class="abs post" style="top:961px">
    <h3>Fusce accumsan, elit a suscipit sagittis, tortor sapien cursus risus..</h3>
    <p>Et interdum lacus lectus et ante.</p>
    <time>on June 04, 2013</time>
  </article>
  <a class="abs more-link" style="left:400px;top:1055px">READ ALL NEWS &gt;&gt;</a>
</section>
<div class="abs vrule" style="left:652px"></div>

<section>
  <a class="abs cv-btn">
    <svg width="40" height="34" viewBox="0 0 40 34">
      <path d="M4 1h22l6 6v26H4z" fill="#fff"/>
      <rect x="4" y="1" width="28" height="7" fill="#d63a2e"/>
      <rect x="0" y="16" width="28" height="13" rx="1" fill="#d63a2e"/>
      <text x="14" y="26.5" font-family="Arial,sans-serif" font-size="10" font-weight="700" fill="#fff" text-anchor="middle">PDF</text>
    </svg>
    <span>DOWNLOAD CV</span>
  </a>
  <h2 class="abs h2" style="left:673px;top:895px">Contact Information</h2>
  <div class="abs info">
    <h4>Office Locations</h4>
    <div>New York/New England</div>
    <div>Baltimore/Washington</div>
    <h4>Contact Us</h4>
    <div>123.456.7890</div>
    <div>123.456.7890</div>
    <h4>Email Us</h4>
    <a>info@tallowanalytics.com</a>
  </div>
</section>

<footer>
  <div class="abs footer"></div>
  <div class="abs f-brand"><span class="brand-mark"></span><span class="brand-name">Tallow Analytics</span></div>
  <div class="abs f-tag">ENGINEERING CONSULTANTS</div>
  <div class="abs copy">Copyright ©2013. All Right Reserved</div>
  <div class="abs connect">Connect Us</div>
  <div class="abs social"><span></span><span></span><span></span><span></span><span></span></div>
</footer>

</body>
</html>
```